BRIGHTWAVE PARTNERS NAMECARD

Need to design a name card with an existing logo.

As we are professional corporate services provider our name card has to project a professional image.
Should be corporate, simple & professional.

Our corporate color is maroon red but not too dull.

Please refer to our website at www.brightwavepartners.com.sg

Would attach our logo herewith.

Front surface of namecard details:
BRIGHTWAVE PARTNERS PTE LTD
Registration No. 208731945K

Lowe Hui Ting CA (Singapore)
Director

Tel +65 6481 2957
Mobile +65 9172 3806
lowe@brightwavepartners.com.sg
www.brightwavepartners.com.sg

47 Palmer Lane
#07-14 Harbourlight Plaza
Singapore 274153

Back of namecard:-
OUR CORE SERVICES
Incorporation services
Corporate Secretarial Services
Accountancy service
Goods & Services Taxation
Corporate & Personal Taxation
Financial Reporting
Payroll Administration

AFFILIATES:
TRIVANTA CORPORATE SERVICES PTE LTD
BRIGHTWAVEREGISTRYPTE LTD
ORR MANAGEMENT SERVICES PTE LTD
DW LIM AND COMPANY PTE LTD
LEDGERWISE ACADEMY

```html
<!DOCTYPE html>
<html lang="en">
<head>
<meta charset="utf-8">
<title>Brightwave Partners Namecard</title>
<link rel="stylesheet" href="https://fonts.googleapis.com/css2?family=Tinos:wght@400;700&display=swap">
<style>
  :root {
    --red: #d0202f;
    --black: #161616;
    --white: #ffffff;
    --ink: #1e1e1e;
    --backdrop: #2a2a2a;
  }
  * { box-sizing: border-box; margin: 0; padding: 0; }
  html, body { width: 1200px; height: 852px; overflow: hidden; }
  body {
    background: var(--backdrop);
    font-family: "Tinos", "Times New Roman", serif;
    position: relative;
  }
  .card {
    position: absolute;
    width: 540px;
    height: 310px;
    border-radius: 22px;
    overflow: hidden;
  }
  /* Brand name placeholder */
  .brand {
    position: absolute;
    display: flex; align-items: center; gap: 8px;
    font-size: 22px; font-weight: 400; line-height: 1;
    white-space: nowrap;
  }
  .brand-mark { width: 12px; height: 12px; flex: none; }

  /* Back */
  .card-back { left: 40px; top: 160px; background: var(--red); }
  .back-top {
    position: absolute; left: 0; top: 0; width: 100%; height: 150px;
    background: var(--black); color: var(--white);
    padding: 34px 34px 0;
  }
  .services-title { font-weight: 700; font-size: 15px; letter-spacing: .3px; margin-bottom: 4px; }
  .services-list { font-size: 12.5px; line-height: 1.45; }
  .services-list .dot { font-size: 9px; vertical-align: 1px; margin: 0 4px; }
  .card-back .brand { right: 30px; top: 176px; color: var(--white); }
  .card-back .brand-mark { background: var(--white); }
  .affiliates {
    position: absolute; left: 34px; top: 186px; color: var(--white);
    font-size: 12px; line-height: 1.35; text-transform: uppercase;
  }
  .affiliates h3 { font-size: 14px; font-weight: 700; margin-bottom: 2px; }

  /* Front */
  .card-front { left: 620px; top: 380px; background: var(--white); }
  .card-front .brand { right: 34px; top: 48px; color: var(--red); font-size: 24px; }
  .card-front .brand-mark { background: var(--red); }
  .name-band {
    position: absolute; left: 0; top: 108px; width: 330px; height: 46px;
    background: var(--red); color: var(--white); padding: 6px 0 0 34px;
  }
  .name-band .name { font-weight: 700; font-size: 17px; line-height: 1.1; }
  .name-band .role { font-size: 12px; }
  .registration { position: absolute; left: 34px; top: 164px; font-size: 14px; color: var(--ink); }
  .address {
    position: absolute; right: 34px; top: 124px; text-align: right;
    font-size: 12.5px; line-height: 1.35; color: var(--ink); font-style: normal;
  }
  .contacts {
    position: absolute; left: 34px; top: 212px; list-style: none;
    font-size: 12.5px; line-height: 1.5; color: var(--ink);
  }
  .contacts li { display: flex; align-items: center; gap: 8px; }
  .contacts svg { width: 11px; height: 11px; fill: var(--red); flex: none; }
  .front-strip { position: absolute; left: 0; bottom: 0; width: 100%; height: 14px; background: var(--red); }
</style>
</head>
<body>

<section class="card card-back">
  <div class="back-top">
    <h2 class="services-title">OUR CORE SERVICES</h2>
    <p class="services-list">
      Incorporation services <span class="dot">●</span> Corporate Secretarial Services <span class="dot">●</span> Accountancy service<br>
      Goods &amp; Services Taxation <span class="dot">●</span> Corporate &amp; Personal Taxation <span class="dot">●</span> Financial Reporting<br>
      Payroll Administration
    </p>
  </div>
  <div class="brand"><span class="brand-mark"></span>Brightwave Partners</div>
  <div class="affiliates">
    <h3>AFFILIATES</h3>
    <p>Trivanta Corporate Services Pte Ltd</p>
    <p>BrightwaveRegistryPte Ltd</p>
    <p>Orr Management Services Pte Ltd</p>
    <p>DW Lim and Company Pte Ltd</p>
    <p>Ledgerwise Academy</p>
  </div>
</section>

<section class="card card-front">
  <div class="brand"><span class="brand-mark"></span>Brightwave Partners</div>
  <div class="name-band">
    <p class="name">Lowe Hui Ting CA (Singapore)</p>
    <p class="role">Director</p>
  </div>
  <p class="registration">Registration No. 208731945K</p>
  <address class="address">
    47 Palmer Lane<br>
    #07-14 Harbourlight Plaza<br>
    Singapore 274153
  </address>
  <ul class="contacts">
    <li><svg viewBox="0 0 12 12"><path d="M2 1l2.5 0 1 3-1.5 1a7 7 0 0 0 3 3l1-1.5 3 1V10a1 1 0 0 1-1 1A9 9 0 0 1 1 2a1 1 0 0 1 1-1z"/></svg>+65 6481 2957</li>
    <li><svg viewBox="0 0 12 12"><path d="M3 0h6a1 1 0 0 1 1 1v10a1 1 0 0 1-1 1H3a1 1 0 0 1-1-1V1a1 1 0 0 1 1-1zm0 2v7h6V2z"/></svg>+65 9172 3806</li>
    <li><svg viewBox="0 0 12 12"><path d="M0 2h12v8H0zm1 1v.3l5 3.4 5-3.4V3z"/></svg>lowe@brightwavepartners.com.sg</li>
    <li><svg viewBox="0 0 12 12"><path d="M6 0a6 6 0 1 0 0 12A6 6 0 0 0 6 0zm-.6 1.2V3.5H3.6a4.8 4.8 0 0 1 1.8-2.3zm1.2 0a4.8 4.8 0 0 1 1.8 2.3H6.6zM2.2 4.7h3.2v2.6H2.2a4.8 4.8 0 0 1 0-2.6zm4.4 0h3.2a4.8 4.8 0 0 1 0 2.6H6.6zM3.6 8.5h1.8v2.3a4.8 4.8 0 0 1-1.8-2.3zm3 0h1.8a4.8 4.8 0 0 1-1.8 2.3z"/></svg>www.brightwavepartners.com.sg</li>
  </ul>
  <div class="front-strip"></div>
</section>

</body>
</html>
```